Web design for online activity booking website

Our activity booking website uTrundle.net is looking outdated and needing a loving revamp on its design and STRUCTURE. it was initially created as a destination guide before we modified the homepage slightly to sell activities. So please DON'T RELY on the current website for your design. Now, the focus is ACTIVITY, while guide/ info should come only as secondary.

In other words, we will be doing something very similar to Plomaro.com (a bit crowded for our liking) and FindMyTrailpal.com. If you could capture the best essences of both, that would be awesome! Besides, we also like nestlo.com's simplicity.

SIMPLE, CLEAN, BRIGHT, USER and MOBILE FRIENDLY please :)

We have a new logo created and some wireframes (a few more in progress) so you know the basic components required in each page. These are just rough ideas so please ignore the ratio/size, colours etc and if you have a better way of arranging or simplifying things, please do so :)

Help us make it a website that everyone would love!

Thank you in advance for your time and artistry.

Target Market(s)

Internet savvy travellers between 18-65

Industry/Entity Type

Tourism

Number of Pages Required

5+ page

Requirements
Must have
• SIMPLE, CLEAN feel, USER and MOBILE FRIENDLY please :)
• See attachments for rough structure. Will also need standard pages such as:
• - About Us
• - Contact Us
• - Wishlist etc
• Message from our developer "designer to keep layers in PSD format accurately so html/css code does not need to lead a mess in photoshop"
Nice to have
• UPDATE: We are so thrilled to receive so many web designs but on the other hand, the submissions are getting too generic and everyone's designs is almost looking identical (many look like they are “borrowed” from existing popular websites). This is making the selection and decision process very difficult.
• So instead of sending us more of the very similar homepage design with minor tweaks (which we can do during handover section anyway), please send us a design of more specific page of our website. Please refer job brief, file no. 5 - Product detail page.
• This will give us better idea of your skills and choose the best as winner to work on the rest of our web pages.
Should not have
• No dark background please

```html
<!DOCTYPE html>
<html lang="en">
<head>
<meta charset="utf-8">
<title>uTrundle.net – Activities</title>
<link rel="stylesheet" href="https://fonts.googleapis.com/css2?family=Roboto+Condensed:wght@400;700&family=Open+Sans:wght@400;600;700&display=swap">
<style>
:root{
  --orange:#f58220;
  --orange-dark:#e06f10;
  --grey-bg:#ebebeb;
  --panel:#e9e9e9;
  --text:#333;
  --muted:#666;
  --footer:#333333;
  --white:#fff;
}
*{box-sizing:border-box;margin:0;padding:0}
html,body{width:1200px;height:3905px;overflow:hidden}
body{font-family:"Open Sans",Arial,sans-serif;color:var(--text);background:var(--white);position:relative}
.abs{position:absolute}
.cond{font-family:"Roboto Condensed","Arial Narrow",sans-serif}
.btn{position:absolute;background:var(--orange);color:#fff;font-family:"Roboto Condensed","Arial Narrow",sans-serif;font-weight:700;font-size:21px;display:flex;align-items:center;justify-content:center;text-transform:uppercase;letter-spacing:.5px}
.section-title{position:absolute;left:78px;font-family:"Roboto Condensed","Arial Narrow",sans-serif;color:var(--orange);font-size:35px;font-weight:400}
.photo{position:absolute}

/* hero */
.hero{position:absolute;left:0;top:0;width:1200px;height:724px;background:linear-gradient(180deg,#9fb0bd 0%,#c9cfd2 22%,#7f8f6a 48%,#4f7a2e 70%,#2f5420 100%)}
.brand{position:absolute;left:78px;top:32px;color:#fff}
.brand-name{font-family:"Roboto Condensed","Arial Narrow",sans-serif;font-weight:700;font-size:60px;line-height:1;display:flex;align-items:center;gap:10px}
.brand-name .dot{width:22px;height:22px;border-radius:50%;background:var(--orange)}
.brand-tag{font-size:11px;font-weight:700;letter-spacing:.5px;margin-top:6px;margin-left:32px;text-transform:uppercase}
.nav{position:absolute;left:409px;top:48px;display:flex;gap:8px;align-items:center;font-family:"Roboto Condensed","Arial Narrow",sans-serif;font-size:18px;color:#fff;text-transform:uppercase}
.nav a{color:#fff;text-decoration:none;padding:8px 10px;display:flex;align-items:center;gap:6px}
.nav a.active{border:1px solid #fff;background:rgba(0,0,0,.15);border-radius:3px}
.flag{width:26px;height:16px;background:linear-gradient(#1f3f8f,#1f3f8f);position:relative;display:inline-block}
.flag:before{content:"";position:absolute;left:0;right:0;top:6px;height:4px;background:#c8102e}
.flag:after{content:"";position:absolute;top:0;bottom:0;left:11px;width:4px;background:#c8102e}
.hero-title{position:absolute;left:0;width:1200px;top:364px;text-align:center;color:#fff;font-family:"Roboto Condensed","Arial Narrow",sans-serif;font-weight:700;font-size:56px;text-shadow:0 2px 4px rgba(0,0,0,.35)}
.hero-sub{position:absolute;left:0;width:1200px;top:424px;text-align:center;color:#fff;font-size:23px}
.select{position:absolute;top:487px;height:42px;background:#d9d9d9;border:1px solid #aaa;font-size:17px;color:#333;display:flex;align-items:center;padding-left:12px;font-family:"Roboto Condensed","Arial Narrow",sans-serif}
.select:after{content:"";position:absolute;right:12px;top:17px;border-left:7px solid transparent;border-right:7px solid transparent;border-top:8px solid #444}

/* grey sections */
.band{position:absolute;left:0;width:1200px}
.grey{background:var(--grey-bg)}

/* activity cards */
.card{position:absolute;top:1512px;width:312px;height:310px;background:#fff;border:1px solid #ddd}
.card .photo{left:0;top:0;width:310px;height:167px}
.card-name{position:absolute;top:175px;width:100%;text-align:center;font-size:18px;font-family:"Roboto Condensed","Arial Narrow",sans-serif}
.card-rate{position:absolute;top:212px;left:0;right:0;border-top:1px solid #ddd;padding:12px 14px 0;display:flex;align-items:center;font-size:14px;color:var(--muted)}
.stars{color:var(--orange);font-size:20px;letter-spacing:1px;margin-right:10px}
.card-rate svg{margin-left:auto}
.card-price{position:absolute;top:260px;left:14px;font-size:21px;font-weight:600;font-family:"Roboto Condensed","Arial Narrow",sans-serif}
.card-book{position:absolute;top:256px;right:14px;width:135px;height:36px;background:var(--orange);color:#fff;font-family:"Roboto Condensed","Arial Narrow",sans-serif;font-size:18px;display:flex;align-items:center;justify-content:center}

/* tours */
.tour{position:absolute;top:2059px;width:312px}
.tour .photo{position:relative;width:312px;height:167px}
.tour-label{height:49px;background:var(--orange);color:#fff;font-family:"Roboto Condensed","Arial Narrow",sans-serif;font-size:27px;display:flex;align-items:center;justify-content:center}

/* blog */
.blog-panel{position:absolute;left:601px;top:2470px;width:521px;height:349px;background:var(--panel);padding:40px 32px}
.blog-title{font-family:"Roboto Condensed","Arial Narrow",sans-serif;color:var(--orange);font-size:36px;line-height:1.1}
.blog-by{font-size:13px;color:var(--muted);margin-top:8px}
.blog-text{font-size:15px;line-height:25px;color:#444;margin-top:14px}
.more{color:var(--orange);font-weight:700;text-decoration:underline;font-size:14px}

/* welcome */
.welcome-title{position:absolute;top:2919px;width:1200px;text-align:center;font-family:"Roboto Condensed","Arial Narrow",sans-serif;color:var(--orange);font-size:38px}
.welcome-text{position:absolute;left:100px;width:1000px;top:2980px;text-align:center;font-size:14.5px;line-height:26px;color:#333}
.welcome-text p{margin-bottom:18px}

/* link columns */
.links{position:absolute;top:3340px;font-size:14.5px;color:#555;line-height:31px;list-style:none}
.links li{padding-left:20px;position:relative}
.links li:before{content:"";position:absolute;left:2px;top:10px;border-top:6px solid transparent;border-bottom:6px solid transparent;border-left:8px solid var(--orange)}
.links li.first{color:var(--orange)}

/* footer */
.footer{position:absolute;left:0;top:3571px;width:1200px;height:334px;background:var(--footer);color:#eee}
.f-col{position:absolute;top:33px}
.f-head{font-family:"Roboto Condensed","Arial Narrow",sans-serif;font-weight:700;font-size:20px;text-transform:uppercase;padding-bottom:4px;border-bottom:2px solid #eee;display:inline-block;margin-bottom:10px}
.f-list{list-style:none;font-size:14.5px;line-height:26px}
.social{display:grid;grid-template-columns:repeat(3,39px);gap:24px 52px;margin-top:10px}
.social span{width:39px;height:39px;border-radius:50%;background:var(--orange);display:block}
.subscribe{position:absolute;left:893px;top:216px;width:229px;height:35px;display:flex}
.subscribe .field{flex:1;background:#fff;color:#555;font-size:12px;display:flex;align-items:center;padding-left:8px}
.subscribe .go{width:52px;background:var(--orange);display:flex;align-items:center;justify-content:center}
.copy{position:absolute;bottom:14px;width:100%;text-align:center;font-size:13px;color:#ddd}
.copy b{color:var(--orange)}
</style>
</head>
<body>

<!-- HERO -->
<header class="hero" role="img" aria-label="Mountain valley landscape with a paraglider above clouds and green forest">
  <div class="brand">
    <div class="brand-name"><span class="dot"></span>uTrundle</div>
    <div class="brand-tag">Your adventure starts here!</div>
  </div>
  <nav class="nav">
    <a class="active" href="#">
      <svg width="18" height="16" viewBox="0 0 18 16"><path d="M9 1 1 8h2v7h4v-5h4v5h4V8h2z" fill="#fff"/></svg>Home</a>
    <a href="#"><svg width="16" height="16" viewBox="0 0 16 16"><path d="M2 14l1-4 8-8 3 3-8 8z" fill="#fff"/></svg>About</a>
    <a href="#"><svg width="18" height="14" viewBox="0 0 18 14"><rect x="1" y="1" width="16" height="12" fill="none" stroke="#fff" stroke-width="2"/><path d="M1 1l8 7 8-7" fill="none" stroke="#fff" stroke-width="2"/></svg>Contact</a>
    <a href="#"><svg width="18" height="16" viewBox="0 0 18 16"><path d="M9 15S1 10 1 5a4 4 0 0 1 8-1 4 4 0 0 1 8 1c0 5-8 10-8 10z" fill="none" stroke="#fff" stroke-width="2"/></svg>Wishlist</a>
    <a href="#"><svg width="12" height="16" viewBox="0 0 12 16"><path d="M2 5a4 4 0 1 1 6 3c-1 1-2 1.5-2 3" fill="none" stroke="#fff" stroke-width="2.5"/><rect x="4.7" y="13" width="2.6" height="2.6" fill="#fff"/></svg>Help</a>
    <a href="#"><svg width="18" height="16" viewBox="0 0 18 16"><path d="M1 8h10M7 4l4 4-4 4" fill="none" stroke="#fff" stroke-width="2.5"/><path d="M11 1h6v14h-6" fill="none" stroke="#fff" stroke-width="2"/></svg>Login</a>
    <a href="#"><span class="flag"></span><svg width="12" height="8" viewBox="0 0 12 8"><path d="M0 0h12L6 8z" fill="#fff"/></svg></a>
  </nav>
  <h1 class="hero-title">LET'S START ACTIVITIES</h1>
  <p class="hero-sub">Your Adventure Starts Here!</p>
  <div class="select" style="left:234px;width:261px">Choose Destination</div>
  <div class="select" style="left:515px;width:261px">Choose An Activities</div>
  <div class="btn" style="left:797px;top:487px;width:166px;height:42px">Let's Go</div>
</header>

<!-- MOST POPULAR DESTINATION -->
<section class="band grey" style="top:724px;height:682px"></section>
<h2 class="section-title" style="top:767px">Most Popular Destination</h2>
<div class="photo" style="left:78px;top:843px;width:240px;height:209px;background:linear-gradient(135deg,#e8a33c,#c9701d)" role="img" aria-label="Tenerife sand dunes"></div>
<div class="abs cond" style="left:78px;top:925px;width:240px;text-align:center;color:#fff;font-size:26px;font-weight:700">Tenerife</div>
<div class="photo" style="left:338px;top:843px;width:240px;height:209px;background:linear-gradient(160deg,#2d7bc4 0%,#b8602e 45%,#d98f4f 75%,#8c9aa0 100%)" role="img" aria-label="Red rock coastline by the sea"></div>
<div class="photo" style="left:78px;top:1072px;width:240px;height:209px;background:linear-gradient(180deg,#5ea7e0 0%,#9dc7e4 35%,#8b7864 55%,#c2a57e 100%)" role="img" aria-label="Sandy beach with mountains behind"></div>
<div class="photo" style="left:338px;top:1072px;width:240px;height:209px;background:linear-gradient(180deg,#4a8fd6 0%,#7fb5dd 30%,#3fb6c7 60%,#1f8fb0 100%)" role="img" aria-label="Boat in turquoise water"></div>
<div class="photo" style="left:622px;top:843px;width:500px;height:438px;background:#e6e2d8;border:2px solid var(--orange)" role="img" aria-label="Map of Tenerife with destination pin"></div>
<div class="btn" style="left:78px;top:1301px;width:148px;height:47px">Show All</div>

<!-- MOST POPULAR ACTIVITIES -->
<h2 class="section-title" style="top:1447px">Most Popular Activities</h2>

<div class="card" style="left:78px">
  <div class="photo" style="background:linear-gradient(180deg,#1b7fd0,#0a3f8e)" role="img" aria-label="Scuba diver underwater"></div>
  <div class="card-name">Diving</div>
  <div class="card-rate"><span class="stars">★★★☆</span>86 Review
    <svg width="22" height="20" viewBox="0 0 22 20"><path d="M11 18S2 12 2 6a5 5 0 0 1 9-2 5 5 0 0 1 9 2c0 6-9 12-9 12z" fill="none" stroke="#888" stroke-width="2"/></svg></div>
  <div class="card-price">$ 120.00</div>
  <div class="card-book">BOOK NOW</div>
</div>
<div class="card" style="left:443px">
  <div class="photo" style="background:linear-gradient(135deg,#a35a3c,#6e3422 60%,#b97a55)" role="img" aria-label="Climber on a red rock face"></div>
  <div class="card-name">Climbing</div>
  <div class="card-rate"><span class="stars">★★★★</span>102 Review
    <svg width="22" height="20" viewBox="0 0 22 20"><path d="M11 18S2 12 2 6a5 5 0 0 1 9-2 5 5 0 0 1 9 2c0 6-9 12-9 12z" fill="none" stroke="#888" stroke-width="2"/></svg></div>
  <div class="card-price">$ 120.00</div>
  <div class="card-book">BOOK NOW</div>
</div>
<div class="card" style="left:809px">
  <div class="photo" style="background:linear-gradient(180deg,#bcd8ee 0%,#8dbcdf 55%,#3f8fbf 100%)" role="img" aria-label="Flyboarder above the sea"></div>
  <div class="card-name">Flyboarding</div>
  <div class="card-rate"><span class="stars">★★★★</span>86 Review
    <svg width="22" height="20" viewBox="0 0 22 20"><path d="M11 18S2 12 2 6a5 5 0 0 1 9-2 5 5 0 0 1 9 2c0 6-9 12-9 12z" fill="none" stroke="#888" stroke-width="2"/></svg></div>
  <div class="card-price">$ 120.00</div>
  <div class="card-book">BOOK NOW</div>
</div>
<div class="btn" style="left:526px;top:1843px;width:148px;height:47px">Show All</div>

<!-- RECOMMENDED TOURS -->
<section class="band grey" style="top:1947px;height:469px"></section>
<h2 class="section-title" style="top:1989px">Recommended Tours And Activities In Spain</h2>
<div class="tour" style="left:78px">
  <div class="photo" style="background:linear-gradient(180deg,#3a7ec6 0%,#88b6d8 40%,#c99a4e 70%,#8a6a3a 100%)" role="img" aria-label="Coastal cliffs and beach"></div>
  <div class="tour-label">Hiking</div>
</div>
<div class="tour" style="left:443px">
  <div class="photo" style="background:linear-gradient(180deg,#5fa0dc 0%,#9ed0e0 35%,#46c0c8 65%,#1d95b5 100%)" role="img" aria-label="Boat on clear turquoise water"></div>
  <div class="tour-label">Boat Tour</div>
</div>
<div class="tour" style="left:809px">
  <div class="photo" style="background:linear-gradient(180deg,#2f6fbf 0%,#8fb5d8 40%,#4a4a3a 60%,#d9cdb4 85%,#3f86b8 100%)" role="img" aria-label="Mountain slope above a sandy beach"></div>
  <div class="tour-label">Hiking</div>
</div>
<div class="btn" style="left:78px;top:2298px;width:148px;height:47px">Show All</div>

<!-- BLOG -->
<div class="photo" style="left:78px;top:2470px;width:523px;height:349px;background:linear-gradient(180deg,#6ea7dc 0%,#c7dbe9 35%,#7b7a5c 55%,#5d6b3a 80%,#4a5a2e 100%)" role="img" aria-label="Winding trail through the Masca gorge mountains"></div>
<article class="blog-panel">
  <h3 class="blog-title">Hiking down the Masca gorge</h3>
  <p class="blog-by">by Mira Holloway (Mimi) — last modified Nov 10, 2014 08:35 PM</p>
  <p class="blog-text">uTrundle and friends venturing down the Masca gorge then kayaking to Los Gigantes.</p>
  <p class="blog-text">It was a cloudy morning in Puerto de la Cruz. I was a little nervous about how the day was going to pan out... <span class="more">READ MORE</span></p>
</article>
<div class="btn" style="left:633px;top:2725px;width:145px;height:45px">View All</div>

<!-- WELCOME -->
<section class="band grey" style="top:2879px;height:411px"></section>
<h2 class="welcome-title">Welcome to uTrundle -- The island travel guide!</h2>
<div class="welcome-text">
  <p>After a couple of years of extensive research in which our team of writers, researchers and IT whiz kids have been beavering away incessantly, we are delighted to welcome you to uTrundle, our definitive guide to the Canary Islands and the Madeira Archipelago.</p>
  <p>Whether you're looking for sun and sand, a hedonistic weekend or consider yourself to be something of a culture vulture, our aim is to provide all the information you need on our favourite islands.</p>
  <p>We are also already looking to the future; soon we hope to bring you further guides on islands from across the world, whilst also allowing the opportunity to book your activities on the islands directly through us, here at uTrundle.net. Please watch this space!</p>
  <p>In the meantime, if you feel that we've missed something or that the site could be improved, please don't hesitate to get in touch.</p>
</div>

<!-- LINK COLUMNS -->
<ul class="links" style="left:78px"><li class="first">Lorem Ipsum is dummy text</li><li>Lorem Ipsum is dummy text</li><li>Lorem Ipsum is dummy text</li><li>Lorem Ipsum is dummy text</li><li>Lorem Ipsum is dummy text</li><li>Lorem Ipsum is dummy text</li></ul>
<ul class="links" style="left:351px"><li class="first">Lorem Ipsum is dummy text</li><li>Lorem Ipsum is dummy text</li><li>Lorem Ipsum is dummy text</li><li>Lorem Ipsum is dummy text</li><li>Lorem Ipsum is dummy text</li><li>Lorem Ipsum is dummy text</li></ul>
<ul class="links" style="left:622px"><li class="first">Lorem Ipsum is dummy text</li><li>Lorem Ipsum is dummy text</li><li>Lorem Ipsum is dummy text</li><li>Lorem Ipsum is dummy text</li><li>Lorem Ipsum is dummy text</li><li>Lorem Ipsum is dummy text</li></ul>
<ul class="links" style="left:893px"><li class="first">Lorem Ipsum is dummy text</li><li>Lorem Ipsum is dummy text</li><li>Lorem Ipsum is dummy text</li><li>Lorem Ipsum is dummy text</li><li>Lorem Ipsum is dummy text</li><li>Lorem Ipsum is dummy text</li></ul>

<!-- FOOTER -->
<footer class="footer">
  <div class="f-col" style="left:78px">
    <div class="f-head">Company</div>
    <ul class="f-list"><li>About uTrundle.net</li><li>Corporate Info</li><li>Site map?</li><li>Blog</li><li>Careers</li></ul>
  </div>
  <div class="f-col" style="left:351px">
    <div class="f-head">Support</div>
    <ul class="f-list"><li>Contact us</li><li>FAQs</li><li>Legal</li><li>Privacy Policy</li><li>Legal</li></ul>
  </div>
  <div class="f-col" style="left:622px">
    <div class="f-head">Partnerships</div>
    <ul class="f-list"><li>Supplier sign-up</li><li>Affiliate Programs</li></ul>
    <div class="f-head" style="margin-top:12px">Log-ins</div>
    <ul class="f-list"><li>Customers</li><li>Suppliers</li><li>Affiliates</li></ul>
  </div>
  <div class="f-col" style="left:893px">
    <div class="f-head">Be Social</div>
    <div class="social"><span></span><span></span><span></span><span></span><span></span><span></span></div>
  </div>
  <div class="subscribe">
    <div class="field">Enter Your Email id here</div>
    <div class="go"><svg width="26" height="18" viewBox="0 0 26 18"><rect x="1" y="1" width="24" height="16" fill="none" stroke="#fff" stroke-width="2"/><path d="M1 1l12 9 12-9" fill="none" stroke="#fff" stroke-width="2"/></svg></div>
  </div>
  <div class="copy">© <b>uTrundle</b> - 2015. All Rights Reserved.</div>
</footer>

</body>
</html>
```